依頼詳細
会社の看板デザインを依頼させて頂きます。看板は国道沿いで、信号待ちに見ていただける場所です。看板から「安さ」「信頼感」「おしゃれ感」が伝わるイメージがあると嬉しいです。使いたいフレーズは「そうだ、家を建てよう」「住まい造りのディベロッパー」です。
記載項目
記載項目:会社名「有限会社 北村建設/北村不動産」
電話番号:099-735-2046
キャッチコピー/「そうだ、家を建てよう」「住まい造りのディベロッパー」
ロゴ/家のマーク(添付ファイル有り・マークを写真に撮ったものなので、そのままは使えません。)
看板サイズ:横 約780cm x 縦 182cm
希望イメージ
シンプル 複雑
単色 カラフル
暗い 明るい
日常 高級
遊び心 厳粛
未来的 伝統的
女性的 男性的
希望する色
茶・オレンジ・アイボリー・赤・白・木目
納品ファイル
• 高解像度JPG (.jpg)
補足説明
ご参考までに。当社のホームページです。http://www.hokuzan-web.jp/kitamura-home
25日・抜けていた添付ファイルを追加しました。
たくさんのご応募ありがとうございます!
弊社外観を追加添付しました。
たくさんのご応募本当にありがとうございます!
社内で検討したところ、「そうだ、家を建てよう」の
コメントを無くすことになりました。
「新築・建替え・貸家経営・空家管理・土地活用、住まいのことなら
何でもおまかせください」といった内容をアピールすることになりました。
この文言では長いので、アレンジはデザイナー様にお任せします。
今になって変更となり大変申し訳ありませんが、
再考していただけるデザイナー様、よろしくお願いいたします。

事務所の雰囲気に合っていて、お客様が店に入りやすい雰囲気を持っていたので決定しました。

多数のご応募、本当にありがとうございました!クオリティーの高さに感激しております。今日までずっと悩み通しました。ミツケルンの利用は初めてでしたので、失礼がありましたらこの場をお借りしてお詫び申し上げます。今後の皆様のご活躍を心よりお祈り申し上げます。

```html
<!DOCTYPE html>
<html lang="ja">
<head>
<meta charset="utf-8">
<title>北村建設 看板デザイン案</title>
<link rel="stylesheet" href="https://fonts.googleapis.com/css2?family=Noto+Sans+JP:wght@700;900&display=swap">
<style>
  :root {
    --brown: #5b3a1d;
    --white: #ffffff;
    --orange: #e8681c;
    --green: #1e9a4b;
    --red: #d61f2b;
    --bg: #ffffff;
  }
  * { margin: 0; padding: 0; box-sizing: border-box; }
  html, body {
    width: 1200px; height: 1200px; overflow: hidden;
    background: var(--bg);
    font-family: "Noto Sans JP", sans-serif;
  }
  .canvas { position: relative; width: 1200px; height: 1200px; }
  .signboard {
    position: absolute; left: 34px; width: 1133px; height: 264px;
    background: var(--brown);
    box-shadow: 2px 3px 6px rgba(0,0,0,0.25);
  }
  .signboard--orange { top: 90px;  --accent: var(--orange); --info: var(--brown); }
  .signboard--green-red { top: 474px; --accent: var(--green); --info: var(--red); }
  .signboard--green { top: 858px; --accent: var(--green); --info: var(--brown); }

  .headline {
    position: absolute; left: 30px; top: 14px;
    color: var(--white); font-weight: 900; font-size: 78px;
    line-height: 104px; letter-spacing: 2px; white-space: nowrap;
  }
  .info-panel {
    position: absolute; left: 0; top: 130px; width: 872px; height: 134px;
    background: var(--white);
  }
  .tagline {
    position: absolute; left: 30px; top: 6px;
    color: var(--accent); font-weight: 900; font-size: 56px;
    line-height: 66px; letter-spacing: 1px; white-space: nowrap;
  }
  .company, .phone {
    position: absolute; top: 83px;
    color: var(--info); font-weight: 700; line-height: 38px; white-space: nowrap;
  }
  .company { left: 30px; font-size: 26px; }
  .phone { left: 530px; font-size: 31px; letter-spacing: 1px; }
  .phone-icon { font-size: 24px; margin-right: 8px; vertical-align: 2px; }

  .brand-mark {
    position: absolute; left: 872px; top: 0; width: 261px; height: 264px;
    display: flex; flex-direction: column; align-items: center; justify-content: center; gap: 18px;
  }
  .brand-dot { width: 86px; height: 86px; border-radius: 50%; background: var(--accent); }
  .brand-name { color: var(--white); font-weight: 900; font-size: 34px; line-height: 1; }
</style>
</head>
<body>
<main class="canvas">

  <section class="signboard signboard--orange">
    <h1 class="headline">そうだ、家を建てよう</h1>
    <div class="info-panel">
      <p class="tagline">住まい造りのディベロッパー</p>
      <p class="company">有限会社 北村建設／北村不動産</p>
      <p class="phone"><span class="phone-icon">☎</span>099-735-2046</p>
    </div>
    <div class="brand-mark">
      <span class="brand-dot"></span>
      <span class="brand-name">北村建設</span>
    </div>
  </section>

  <section class="signboard signboard--green-red">
    <h1 class="headline">そうだ、家を建てよう</h1>
    <div class="info-panel">
      <p class="tagline">住まい造りのディベロッパー</p>
      <p class="company">有限会社 北村建設／北村不動産</p>
      <p class="phone"><span class="phone-icon">☎</span>099-735-2046</p>
    </div>
    <div class="brand-mark">
      <span class="brand-dot"></span>
      <span class="brand-name">北村建設</span>
    </div>
  </section>

  <section class="signboard signboard--green">
    <h1 class="headline">そうだ、家を建てよう</h1>
    <div class="info-panel">
      <p class="tagline">住まい造りのディベロッパー</p>
      <p class="company">有限会社 北村建設／北村不動産</p>
      <p class="phone"><span class="phone-icon">☎</span>099-735-2046</p>
    </div>
    <div class="brand-mark">
      <span class="brand-dot"></span>
      <span class="brand-name">北村建設</span>
    </div>
  </section>

</main>
</body>
</html>
```